New Organic Skin Care Line Needs to Design a Product Label

***THE WINNER OF THIS PROJECT WILL MOST LIKELY BECOME THE EXCLUSIVE DESIGNER FOR OUR OTHER PRODUCT LABELS***

We need a label design for a new organic skin care product line called "Maple Fern Gala." This specific product is a 100% pure organic coconut oil. It's used for skin hydration, protection, and makeup removal.

Info to include on front label:

1. Logo: Maple Fern Gala (attached)
2. Product Name: Pure Coconut Oil (emphasize "organic" somewhere)
3. Slogan: Hydrate your skin and hair.
4. Size: 8 FL OZ 236mL

Attached is:

1. The brand logo "Maple Fern Gala" with a white background.
2. An image of the bottle we will use.
3. An image of the bottle with lines to show the size and placement of the label.
4. The brand logo "Maple Fern Gala" with a black background. (photoshop file)

What we need:

A simple mock up of the front side of the label on the bottle. We first want to know what it will look like on the bottle given the size and dimensions.

- We would like one label with a white background (including the logo with a white background).
- We would like a second label with a black background (including the logo with a black background, just need to make the black font white instead of black).

We can get a great idea of what to expect from the front side of the label so we will complete the back side once we identify a winner.
Updates

Apologies, but we are now using a different bottle. The previous one is now discontinued. Please view the two most recent images uploaded. One is an image of the new bottle by itself. The other is an image of that bottle with instructions. Please use your most recent designs on the new bottle. Feel free to make any modifications you see fit to compliment the new bottle shape. Added Friday, March 18, 2016

Reason: We are still working with the label company to finalize the size. Once the size is confirmed we will have to tweak labels based on finalized measurements.

Target Market(s)

Women, 18-70

Industry/Entity Type

Skin Care Product

Font styles to use
Decorative
Script

Requirements
Must have
• -"shabby sheek" and "cute" theme
• -soft organic feel
• -the ingredients are organic, pure, and natural. That should be an essence of the label.

```html
<!DOCTYPE html>
<html lang="en">
<head>
<meta charset="utf-8">
<title>Maple Fern Gala – Pure Coconut Oil Label</title>
<link rel="stylesheet" href="https://fonts.googleapis.com/css2?family=Cinzel:wght@400;700&family=Lobster+Two:wght@700&display=swap">
<style>
  :root {
    --canvas-bg: #f2f2f2;
    --label-bg: #ffffff;
    --ink: #231f20;
    --brand-pink: #e8197a;
    --art-light: #d8c7ad;
    --art-dark: #b39a78;
    --rule: #231f20;
  }
  * { margin: 0; padding: 0; box-sizing: border-box; }
  html, body {
    width: 716px;
    height: 1200px;
    overflow: hidden;
    background: var(--canvas-bg);
  }
  .canvas {
    position: relative;
    width: 716px;
    height: 1200px;
  }
  .label {
    position: absolute;
    left: 137px;
    top: 468px;
    width: 440px;
    height: 512px;
    background: var(--label-bg);
    box-shadow: 0 1px 4px rgba(0,0,0,0.08);
  }
  .brand-mark {
    position: absolute;
    left: 198px;
    top: 34px;
    width: 44px;
    height: 44px;
    border-radius: 50%;
    background: var(--brand-pink);
  }
  .brand-name {
    position: absolute;
    top: 114px;
    left: 0;
    width: 100%;
    text-align: center;
    font-family: "Cinzel", serif;
    font-weight: 400;
    font-size: 17px;
    letter-spacing: 2.5px;
    color: var(--ink);
  }
  .product-title { margin: 0; }
  .product-name {
    position: absolute;
    left: 0;
    width: 100%;
    text-align: center;
    font-family: "Lobster Two", cursive;
    font-weight: 700;
    color: var(--ink);
    line-height: 1;
  }
  .product-name--pure { top: 164px; font-size: 62px; left: -26px; }
  .product-name--coconut { top: 222px; font-size: 76px; }
  .product-name--oil { top: 288px; font-size: 60px; }
  .coconut-art {
    position: absolute;
    left: 263px;
    top: 167px;
    width: 80px;
    height: 55px;
    border-radius: 8px;
    background: linear-gradient(180deg, var(--art-light), var(--art-dark));
  }
  .tagline {
    position: absolute;
    top: 366px;
    left: 0;
    width: 100%;
    text-align: center;
    font-family: "Cinzel", serif;
    font-weight: 400;
    font-size: 19px;
    letter-spacing: 0.8px;
    color: var(--ink);
  }
  .badge-rules {
    position: absolute;
    left: 0;
    top: 405px;
    width: 440px;
    height: 70px;
  }
  .badge-text {
    position: absolute;
    top: 417px;
    left: 0;
    width: 100%;
    text-align: center;
    font-family: "Lobster Two", cursive;
    font-weight: 700;
    font-size: 42px;
    color: var(--brand-pink);
    line-height: 1;
  }
  .volume {
    position: absolute;
    top: 488px;
    left: 0;
    width: 100%;
    text-align: center;
    font-family: "Cinzel", serif;
    font-weight: 700;
    font-size: 12px;
    color: var(--ink);
  }
</style>
</head>
<body>
<main class="canvas">
  <section class="label">
    <div class="brand-mark" aria-hidden="true"></div>
    <p class="brand-name">Maple Fern Gala</p>

    <h1 class="product-title">
      <span class="product-name product-name--pure">Pure</span>
      <span class="product-name product-name--coconut">Coconut</span>
      <span class="product-name product-name--oil">Oil</span>
    </h1>
    <div class="coconut-art" role="img" aria-label="Illustration of a whole and halved coconut with green leaves"></div>

    <p class="tagline">HYDRATE YOUR SKIN AND HAIR</p>

    <svg class="badge-rules" viewBox="0 0 440 70" aria-hidden="true">
      <line x1="0" y1="40" x2="120" y2="40" stroke="var(--rule)" stroke-width="1.5"/>
      <line x1="320" y1="40" x2="440" y2="40" stroke="var(--rule)" stroke-width="1.5"/>
      <rect x="120" y="8" width="200" height="58" rx="10" fill="none" stroke="var(--rule)" stroke-width="1.5"/>
    </svg>
    <p class="badge-text">Organic</p>

    <p class="volume">236 ML</p>
  </section>
</main>
</body>
</html>
```